Short-Term Rental Website - Management Services for Property Owner

We are looking for a website to advertise our short-term rental business, Bright Door Rental Management, currently www.brightdoorstays.ca. Hosted on WordPress.

We have the website main page language but we are looking for someone who is creative and can present the information in a trendy, cool and professional way. I like the closed design crowd job "Plumwick Media - SEM, Influencer website. FUN RETRO VIBES" (see attached pictures) in terms of how the page flows, icons and stock images, other connective imagery and design features

Our main competitor website is www.hostvela.com and we like how that website feels but we like the elegance of www.Torvane-Alsky.com (desktop) and main page of www.quorrin.ca (desktop version). We like the slow type video on quorrin.com.

MUST LOOK GOOD ON MOBILE. The mobile experience has to be good.

The content in terms of the language is in one of the attached files.

Our landing page requires the following sections;
- Revenue Maximization
- Services (I have included the content that we want highlighted but we are looking for someone to be creative with how these are displayed
- Pricing
- Featured Properties (display on a carousel) *must design a carousel that can be easily populated.
- Reviews (display on a carousel) *must design a carousel that can be easily populated.
- Contact Us (first name, last name, email, phone (required), description of property)

The header will have;
- Logo (link to main page)
- Pricing (link to pricing section found on the main page)
- Services (link to services section found on the main page)
- Properties (separate page)
- Contact (link to contact area on main page)

We would also need a coded template page that we could use to add additional pages as needed.

For the properties page, we need a landing page that would allow our guests to see all of our properties and a map view with the properties plotted on the map.

As we would collect personal information we would need a cookies/ privacy policy.

The colour palette should be on the light side. We do not want the website to have a dark feel. Colours should be consistent with that of our logo but we are open to creativity.

Investment property owners

Real Estate

2 page

Sans Serif

• Very strong and well designed landing page

Second page which showcases properttes

Template property page that can be easily reproduced

```html
<!DOCTYPE html>
<html lang="en">
<head>
<meta charset="utf-8">
<title>Bright Door Rental Management</title>
<link href="https://fonts.googleapis.com/css2?family=Poppins:wght@400;500;600;700&family=Roboto:wght@300;400;500&family=Roboto+Condensed:wght@400&display=swap" rel="stylesheet">
<style>
:root{
  --teal:#3f6b76;
  --teal-dark:#2f5660;
  --teal-soft:#dde5e7;
  --blush:#f4eff0;
  --ink:#2c2c2c;
  --body:#4a4a4a;
  --muted:#8a8a8a;
  --line:#d9d9d9;
  --white:#ffffff;
  --footer:#2b2b2b;
}
*{box-sizing:border-box;margin:0;padding:0}
html,body{width:1200px;height:3994px;overflow:hidden}
body{position:relative;background:var(--white);font-family:"Roboto",sans-serif;color:var(--body)}
h2.section-title{position:absolute;left:0;width:1200px;text-align:center;font-family:"Poppins",sans-serif;font-weight:700;font-size:22px;color:var(--teal);letter-spacing:-.3px}
.title-rule{position:absolute;left:586px;width:28px;height:3px;background:var(--teal)}

/* header */
.site-header{position:absolute;left:0;top:0;width:1200px;height:117px;background:var(--white)}
.brand{position:absolute;left:132px;top:24px;display:flex;align-items:center;gap:12px}
.brand-mark{width:44px;height:44px;background:var(--teal);border-radius:4px}
.brand-name{font-family:"Poppins",sans-serif;font-weight:700;color:var(--teal);line-height:1}
.brand-name .big{display:block;font-size:40px;letter-spacing:-1px}
.brand-name .small{display:block;font-size:12px;letter-spacing:3px;margin-top:4px}
.head-label{position:absolute;top:20px;font-family:"Poppins",sans-serif;font-size:11px;font-weight:500;color:var(--teal)}
.social-row{position:absolute;left:772px;top:37px;display:flex;gap:4px}
.social-row span{width:28px;height:29px;background:var(--teal);border-radius:4px}
.call-pill{position:absolute;left:904px;top:37px;width:164px;height:30px;background:var(--teal);border-radius:5px;color:#fff;font-family:"Roboto Condensed",sans-serif;font-size:21px;display:flex;align-items:center;padding-left:8px;gap:6px}
.main-nav{position:absolute;top:86px;left:0;width:1200px;font-family:"Poppins",sans-serif;font-size:14px;font-weight:500;color:var(--ink)}
.main-nav a{position:absolute;color:var(--ink);text-decoration:none;letter-spacing:.3px}
.main-nav a.active{color:var(--teal);border-bottom:2px solid var(--teal);padding-bottom:2px}

/* hero */
.hero{position:absolute;left:0;top:117px;width:1200px;height:545px;background:linear-gradient(180deg,#2e5fa8 0%,#4d7bbf 22%,#3a4a3d 45%,#7f7766 65%,#8b8070 82%,#5d5a50 100%)}
.hero h1{position:absolute;left:0;top:45px;width:1200px;text-align:center;font-family:"Poppins",sans-serif;font-weight:700;font-size:23px;line-height:32px;color:#fff;text-transform:uppercase;text-shadow:0 1px 3px rgba(0,0,0,.35)}
.hero-dots{position:absolute;top:506px;left:552px;display:flex;gap:12px;align-items:center}
.hero-dots i{width:8px;height:8px;border-radius:50%;background:#fff;display:block}
.hero-dots i.on{width:12px;height:12px;background:transparent;border:2px solid #fff}

/* services */
.services{position:absolute;left:0;top:662px;width:1200px;height:849px;background:var(--blush)}
.orbit{position:absolute;left:0;top:0}
.svc-icon{position:absolute;width:68px;height:68px;border-radius:50%;background:var(--teal);display:flex;align-items:center;justify-content:center}
.svc-title{position:absolute;text-align:center;font-family:"Poppins",sans-serif;font-weight:600;font-size:14px;line-height:18px;color:var(--ink)}
.svc-text{position:absolute;text-align:center;font-size:11px;line-height:13.5px;color:var(--body)}
.hub-outer{position:absolute;left:478px;width:234px;height:234px;border-radius:50%;border:3px solid #fff;background:#eef1f2;box-shadow:0 0 0 1px #d5dcde}
.hub-inner{position:absolute;left:500px;width:190px;height:190px;border-radius:50%;background:var(--teal-soft)}
.feature-card{position:absolute;top:1257px;width:218px;height:270px;background:#fff;padding:26px 10px 0 22px}
.feature-card h3{font-family:"Poppins",sans-serif;font-weight:600;font-size:13.5px;letter-spacing:-.2px;white-space:nowrap;color:var(--ink);margin:18px 0 10px}
.feature-card ul{list-style:none;padding-right:10px}
.feature-card li{position:relative;padding-left:16px;font-size:10.5px;line-height:13px;color:var(--body);margin-bottom:9px}
.feature-card li::before{content:"";position:absolute;left:2px;top:3px;width:6px;height:3px;border-left:1.5px solid var(--teal);border-bottom:1.5px solid var(--teal);transform:rotate(-45deg)}
.read-more{position:absolute;left:40px;top:243px;font-family:"Poppins",sans-serif;font-size:9px;font-weight:600;color:var(--teal);text-decoration:underline}

/* properties */
.prop-card{position:absolute;top:1676px;width:225px;height:351px;background:#fff;border:1px solid var(--line);border-radius:4px;overflow:hidden}
.prop-photo{height:214px}
.prop-body{padding:10px 17px}
.stars{font-size:10px;color:var(--teal);letter-spacing:1px}
.stars small{color:var(--body);font-size:9.5px;letter-spacing:0;margin-left:4px}
.prop-name{font-family:"Poppins",sans-serif;font-size:12px;font-weight:500;line-height:15px;color:var(--ink);margin-top:9px;height:30px}
.prop-price{font-family:"Poppins",sans-serif;font-weight:600;font-size:14px;color:var(--teal);margin-top:10px}
.pill{display:inline-block;margin-top:5px;background:var(--teal);color:#fff;font-family:"Poppins",sans-serif;font-size:8px;font-weight:600;padding:3px 9px;border-radius:3px}
.carousel-nav{position:absolute;top:2060px;left:544px;display:flex;align-items:center;gap:5px}
.carousel-nav i{width:6px;height:6px;border-radius:50%;background:#9aa9ad;display:block}
.carousel-nav i.on{background:var(--teal);width:7px;height:7px}

/* pricing */
.pricing{position:absolute;left:0;top:2137px;width:639px;height:517px;background:var(--teal);color:#fff}
.pricing-photo{position:absolute;left:639px;top:2137px;width:561px;height:517px;background:linear-gradient(180deg,#7ea3c9 0%,#4f6a3c 30%,#8a4a3a 50%,#7a4134 62%,#3f7a2c 78%,#5a9a35 100%)}
.pricing h2{position:absolute;left:130px;top:46px;font-family:"Poppins",sans-serif;font-weight:700;font-size:20px}
.pricing .sub{position:absolute;left:130px;top:76px;font-family:"Roboto",sans-serif;font-weight:300;font-size:21px}
.pct{position:absolute;left:128px;top:160px;font-family:"Roboto Condensed",sans-serif;font-size:74px;line-height:1}
.pct-rule{position:absolute;left:284px;top:141px;width:1px;height:140px;background:rgba(255,255,255,.6)}
.perk{position:absolute;left:310px;display:flex;gap:18px;align-items:center;font-size:12px;line-height:17px}
.perk .ico{width:34px;height:34px;border-radius:50%;background:#fff;flex:none;display:flex;align-items:center;justify-content:center}
.note{position:absolute;left:129px;width:451px;height:63px;background:rgba(255,255,255,.1);display:flex;align-items:center;gap:14px;padding-left:14px;font-size:12px;line-height:16px;color:#dbe6e8}
.note .ring{width:22px;height:22px;border:1.5px solid #fff;border-radius:50%;flex:none;display:flex;align-items:center;justify-content:center}

/* reviews */
.reviews{position:absolute;left:0;top:2654px;width:1200px;height:493px;background:var(--blush)}
.review-card{position:absolute;top:2778px;width:302px;height:273px;background:#fff;padding:22px 22px 0 22px;box-shadow:0 1px 4px rgba(0,0,0,.06)}
.quote-mark{font-family:"Poppins",sans-serif;font-size:34px;line-height:20px;color:#b9b9b9;height:20px}
.review-card p{margin:2px 0 0 24px;font-size:12.5px;line-height:17.5px;color:var(--body)}
.review-card .stars{position:absolute;left:46px;top:176px;font-size:12px}
.reviewer{position:absolute;left:46px;top:210px;display:flex;align-items:center;gap:12px}
.avatar{width:38px;height:38px;border-radius:50%;background:linear-gradient(135deg,#c9b9a9,#6f6258)}
.reviewer b{display:block;font-weight:400;font-size:12.5px;color:var(--ink)}
.reviewer small{font-size:10px;color:var(--muted)}
.arrow{position:absolute;font-family:"Roboto",sans-serif;font-weight:300;font-size:44px;color:#a9a9a9}
.town-strip{position:absolute;left:0;top:3061px;width:1200px;height:86px;background:linear-gradient(180deg,rgba(223,217,219,.4),rgba(223,217,219,.9))}

/* contact */
.contact{position:absolute;left:0;top:3147px;width:1200px;height:491px;background:linear-gradient(180deg,#f8f6f7,#fbfafa)}
.field{position:absolute;background:#fff;border:1px solid #cfcfcf;font-size:13px;color:var(--ink);padding:13px 16px}
.submit{position:absolute;left:538px;top:3548px;width:124px;height:39px;background:var(--teal);color:#fff;font-family:"Poppins",sans-serif;font-weight:700;font-size:15px;display:flex;align-items:center;justify-content:center;border-radius:2px}

/* footer */
.site-footer{position:absolute;left:0;top:3638px;width:1200px;height:356px;background:var(--footer);color:#fff}
.site-footer .brand{left:132px;top:98px}
.site-footer .brand-mark{background:#fff}
.site-footer .brand-name{color:#fff}
.foot-head{position:absolute;top:54px;font-family:"Poppins",sans-serif;font-weight:700;font-size:12.5px;letter-spacing:.5px}
.foot-menu{position:absolute;left:519px;top:90px;list-style:none;font-size:11.5px;line-height:20px;letter-spacing:.3px}
.foot-item{position:absolute;display:flex;gap:12px;align-items:center;font-size:11.5px;line-height:15px}
.foot-item .dot{width:22px;height:22px;border-radius:50%;background:#fff;flex:none;display:flex;align-items:center;justify-content:center}
.copyright{position:absolute;left:0;top:3949px;width:1200px;text-align:center;font-size:9.5px;color:#cfcfcf}
</style>
</head>
<body>

<header class="site-header">
  <div class="brand">
    <span class="brand-mark"></span>
    <div class="brand-name"><span class="big">Bright Door</span><span class="small">Rental Management</span></div>
  </div>
  <span class="head-label" style="left:772px">FOLLOW US</span>
  <div class="social-row"><span></span><span></span><span></span></div>
  <span class="head-label" style="left:904px">CALL US</span>
  <div class="call-pill">
    <svg width="20" height="20" viewBox="0 0 24 24"><path fill="#fff" d="M6.6 10.8a15 15 0 006.6 6.6l2.2-2.2c.3-.3.7-.4 1-.2 1.1.4 2.3.6 3.6.6.6 0 1 .4 1 1V20c0 .6-.4 1-1 1A17 17 0 013 4c0-.6.4-1 1-1h3.5c.6 0 1 .4 1 1 0 1.3.2 2.5.6 3.6.1.3 0 .7-.2 1z"/></svg>
    587-210-4418
  </div>
  <nav class="main-nav">
    <a class="active" style="left:515px">HOME</a>
    <a style="left:586px">SERVICES</a>
    <a style="left:688px">PROPERTIES</a>
    <a style="left:809px">PRICING</a>
    <a style="left:904px">REVIEWS</a>
    <a style="left:1003px">CONTACT</a>
  </nav>
</header>

<section class="hero" role="img" aria-label="Photo of a two-storey suburban house with grey siding, white garage door and tall trees under a blue sky">
  <h1>Your property’s value will be optimized to reach its<br>potential through our revenue maximizationservices.</h1>
  <div class="hero-dots"><i></i><i></i><i class="on"></i><i></i><i></i></div>
</section>

<section class="services">
  <svg class="orbit" width="1200" height="849" viewBox="0 0 1200 849">
    <circle cx="600" cy="446" r="478" fill="none" stroke="#e3dcdd" stroke-width="1.5"/>
    <circle cx="600" cy="446" r="448" fill="none" stroke="#ebe5e6" stroke-width="1"/>
    <path d="M330 260 A330 330 0 0 1 870 260" fill="none" stroke="#e0d9da" stroke-width="1.5"/>
  </svg>
</section>
<h2 class="section-title" style="top:708px">OUR SERVICES</h2>
<div class="title-rule" style="top:745px"></div>

<div class="svc-icon" style="left:566px;top:788px">
  <svg width="34" height="30" viewBox="0 0 34 30"><rect x="6" y="8" width="22" height="18" fill="none" stroke="#fff" stroke-width="2"/><path d="M3 10L17 2l14 8" fill="none" stroke="#fff" stroke-width="2"/><rect x="10" y="14" width="4" height="5" fill="#fff"/><rect x="20" y="14" width="4" height="5" fill="#fff"/><rect x="15" y="18" width="4" height="8" fill="#fff"/></svg>
</div>
<div class="svc-title" style="left:450px;top:880px;width:300px">Proprietary Pricing Tool</div>
<div class="svc-text" style="left:455px;top:908px;width:290px">We have developed a proprietary pricing tool that allows us to determine future nightly rates based on demand. This tool has led us to managing the #1 &amp; #5 Highest Revenue 2-Bedroom Listings in Calgary.</div>

<div class="svc-icon" style="left:276px;top:984px">
  <svg width="34" height="30" viewBox="0 0 34 30"><path d="M3 6h10M3 12h8M3 18h8M3 24h12" stroke="#fff" stroke-width="2"/><circle cx="21" cy="14" r="7" fill="none" stroke="#fff" stroke-width="2"/><path d="M26 19l5 6" stroke="#fff" stroke-width="2.5"/></svg>
</div>
<div class="svc-title" style="left:180px;top:1078px;width:260px">StayNest Search<br>Engine Optimization</div>
<div class="svc-text" style="left:190px;top:1127px;width:240px">StayNest ranks all listings using an algorithm (much like Seekly) and our optimization techniques allow your listing to appear higher in search results and receive more bookings.</div>

<div class="svc-icon" style="left:860px;top:984px">
  <svg width="32" height="30" viewBox="0 0 32 30"><rect x="3" y="5" width="26" height="22" rx="2" fill="none" stroke="#fff" stroke-width="2"/><path d="M3 11h26M9 2v6M23 2v6" stroke="#fff" stroke-width="2"/><g fill="#fff"><rect x="7" y="14" width="3" height="3"/><rect x="12" y="14" width="3" height="3"/><rect x="17" y="14" width="3" height="3"/><rect x="22" y="14" width="3" height="3"/><rect x="7" y="20" width="3" height="3"/><rect x="12" y="20" width="3" height="3"/><rect x="17" y="20" width="3" height="3"/></g></svg>
</div>
<div class="svc-title" style="left:766px;top:1078px;width:260px">Strategic Calendar<br>Management</div>
<div class="svc-text" style="left:776px;top:1127px;width:240px">Our strategy focuses on future bookings being as long as possible. This, along with other techniques, has resulted iin our properties averaging an ~85% occupancy rate which is ~20% above market average.</div>

<div class="hub-outer" style="top:992px"></div>
<div class="hub-inner" style="top:1014px"></div>

<article class="feature-card" style="left:144px">
  <svg width="46" height="46" viewBox="0 0 46 46"><circle cx="15" cy="10" r="8" fill="#3f6b76"/><path d="M2 40c0-10 6-17 13-17s13 7 13 17z" fill="#3f6b76"/><circle cx="33" cy="26" r="8" fill="#fff" stroke="#3f6b76" stroke-width="2"/><path d="M33 21l1.6 3.3 3.6.5-2.6 2.5.6 3.6-3.2-1.7-3.2 1.7.6-3.6-2.6-2.5 3.6-.5z" fill="#3f6b76"/></svg>
  <h3>Guest Experience</h3>
  <ul><li>End-to-end management of the guest experience</li><li>Local Calgary Experts (events, guidebook, advice)</li><li>Rapid response time to guest messages</li></ul>
  <span class="read-more">READ MORE</span>
</article>
<article class="feature-card" style="left:370px">
  <svg width="46" height="46" viewBox="0 0 46 46"><path d="M10 14L20 5l10 9v12H10z" fill="#3f6b76"/><path d="M4 32h12l6 4h14v6H4z" fill="#3f6b76"/></svg>
  <h3>Home Care</h3>
  <ul><li>Professional cleaning with unique cleaning guide</li><li>Staging guide created for consistent appearance</li><li>Inventory and replenishment of essentials</li></ul>
  <span class="read-more">READ MORE</span>
</article>
<article class="feature-card" style="left:597px">
  <svg width="46" height="46" viewBox="0 0 46 46"><path d="M19 4l15 5v12c0 10-7 17-15 20C11 38 4 31 4 21V9z" fill="#3f6b76"/><path d="M19 8v28c6-3 11-8 11-15V12z" fill="#fff" opacity=".35"/></svg>
  <h3>Safety &amp; Security</h3>
  <ul><li>Sensory Security Devices (non-invasive, real-time data)</li><li>Insurance for damage provided by StayNest*</li><li>Ongoing Guest Risk Assessment</li></ul>
  <span class="read-more">READ MORE</span>
</article>
<article class="feature-card" style="left:823px">
  <svg width="46" height="46" viewBox="0 0 46 46"><g transform="translate(21 21)"><circle r="13" fill="#3f6b76"/><g fill="#3f6b76"><rect x="-4" y="-19" width="8" height="8"/><rect x="-4" y="11" width="8" height="8"/><rect x="-19" y="-4" width="8" height="8"/><rect x="11" y="-4" width="8" height="8"/><rect x="-4" y="-19" width="8" height="8" transform="rotate(45)"/><rect x="-4" y="11" width="8" height="8" transform="rotate(45)"/><rect x="-19" y="-4" width="8" height="8" transform="rotate(45)"/><rect x="11" y="-4" width="8" height="8" transform="rotate(45)"/></g><circle r="5" fill="#fff"/></g></svg>
  <h3>Performance Optimization</h3>
  <ul><li>Proprietary Pricing Tool used Only by Bright Door</li><li>Strategic Calendar Management</li><li>#1 &amp; #5 Highest Revenue 2-Bedroom Listings in Calgary</li></ul>
  <span class="read-more">READ MORE</span>
</article>

<h2 class="section-title" style="top:1586px">FEATURED PROPERTIES</h2>
<div class="title-rule" style="top:1630px"></div>

<article class="prop-card" style="left:130px">
  <div class="prop-photo" role="img" aria-label="Lakefront backyard with wooden dock, lounge chairs and trees" style="background:linear-gradient(180deg,#b9c3cc 0%,#6f7f5c 40%,#8b7a66 70%,#5f6b70 100%)"></div>
  <div class="prop-body"><div class="stars">★★★★★<small>(13 Reviews)</small></div><div class="prop-name">Pine Shore Hideaway<br>Lakeside w/ pier &amp; cinema</div><div class="prop-price">₹35767</div><span class="pill">READ MORE</span></div>
</article>
<article class="prop-card" style="left:367px">
  <div class="prop-photo" role="img" aria-label="Bright living room with grey sofa, curtains and round coffee table" style="background:linear-gradient(180deg,#dfe3e4 0%,#b9c4c9 45%,#8f9aa0 75%,#c7b9a6 100%)"></div>
  <div class="prop-body"><div class="stars">★★★★★<small>(13 Reviews)</small></div><div class="prop-name">The Amber Manor -<br>3 beds, parking &amp; deck</div><div class="prop-price">₹7342</div><span class="pill">READ MORE</span></div>
</article>
<article class="prop-card" style="left:605px">
  <div class="prop-photo" role="img" aria-label="Rooftop terrace with outdoor sofas, glass railing and city towers" style="background:linear-gradient(180deg,#c9cfd4 0%,#8d969c 35%,#5e7a55 60%,#7c7770 100%)"></div>
  <div class="prop-body"><div class="stars">★★★★★<small>(13 Reviews)</small></div><div class="prop-name">PRIVATE Terrace in Lovely<br>Riverside + Parking</div><div class="prop-price">₹16607</div><span class="pill">READ MORE</span></div>
</article>
<article class="prop-card" style="left:842px">
  <div class="prop-photo" role="img" aria-label="Living room with blue sofa, wall clock and large windows" style="background:linear-gradient(180deg,#e8ecef 0%,#c4ccd3 40%,#6b7fa0 70%,#b2a99d 100%)"></div>
  <div class="prop-body"><div class="stars">★★★★★<small>(13 Reviews)</small></div><div class="prop-name">Quiet 2Bed w/TV &amp; Parking<br>near Downtown Core!</div><div class="prop-price">₹6663</div><span class="pill">READ MORE</span></div>
</article>
<div class="carousel-nav">
  <svg width="14" height="20" viewBox="0 0 14 20"><path d="M11 2L3 10l8 8" fill="none" stroke="#9a9a9a" stroke-width="2"/></svg>
  <i class="on"></i><i></i><i></i><i></i><i></i><i></i>
  <svg width="14" height="20" viewBox="0 0 14 20"><path d="M3 2l8 8-8 8" fill="none" stroke="#9a9a9a" stroke-width="2"/></svg>
</div>

<section class="pricing">
  <h2>PRICING</h2>
  <div class="sub">Bright Door's share of the nightly revenue</div>
  <div class="pct">20%</div>
  <div class="pct-rule"></div>
  <div class="perk" style="top:141px"><span class="ico"><svg width="20" height="18" viewBox="0 0 20 18"><path d="M1 6L10 1l9 5z" fill="#3f6b76"/><path d="M3 8v7M7 8v7M13 8v7M17 8v7M1 17h18" stroke="#3f6b76" stroke-width="2"/></svg></span><span>All money goes to your bank account,<br>we invoice you one-time per month</span></div>
  <div class="perk" style="top:194px"><span class="ico"><svg width="22" height="22" viewBox="0 0 22 22"><circle cx="11" cy="11" r="8" fill="none" stroke="#3f6b76" stroke-width="2.5"/><path d="M5.5 5.5l11 11" stroke="#3f6b76" stroke-width="2.5"/></svg></span><span>There are no additionalfees and<br>best of all, no surprises!</span></div>
  <div class="perk" style="top:250px"><span class="ico"><svg width="22" height="22" viewBox="0 0 22 22"><circle cx="12" cy="8" r="6" fill="#3f6b76"/><text x="12" y="11" text-anchor="middle" font-size="8" font-family="Roboto,sans-serif" fill="#fff">$</text><path d="M2 17h6l4 2h6l2-3" fill="none" stroke="#3f6b76" stroke-width="2"/></svg></span><span>Our pricing structure is simple and<br>easy to understand, that is by design!</span></div>
  <div class="note" style="top:331px"><span class="ring"><svg width="10" height="8" viewBox="0 0 10 8"><path d="M1 4l3 3 5-6" fill="none" stroke="#fff" stroke-width="1.5"/></svg></span><span>The nightly revenue is split between the Owner and Bright Door,<br>80% &amp; 20% respectively.</span></div>
  <div class="note" style="top:407px"><span class="ring"><svg width="10" height="8" viewBox="0 0 10 8"><path d="M1 4l3 3 5-6" fill="none" stroke="#fff" stroke-width="1.5"/></svg></span><span>The cleaning fee is paid for by the guest which covers all cleaning<br>between guests. We do not take a fee from cleaning.</span></div>
</section>
<div class="pricing-photo" role="img" aria-label="Red-brick two-storey house with white windows, green lawn and tall trees"></div>

<section class="reviews"></section>
<h2 class="section-title" style="top:2699px">REVIEWS</h2>
<div class="title-rule" style="top:2742px"></div>
<span class="arrow" style="left:76px;top:2874px">‹</span>
<span class="arrow" style="left:1094px;top:2874px">›</span>

<article class="review-card" style="left:126px">
  <div class="quote-mark">“</div>
  <p>At vero eos et accusamus et iusto odio dignissimos ducimus qui blan ditiis praesentium voluptatum deleniti atque corrupti quos dolores et quas moles tias excepturi sint occaecati cupiditate non provident, similique sunt in culpa qui.</p>
  <div class="stars">★★★★★</div>
  <div class="reviewer"><span class="avatar" role="img" aria-label="Reviewer portrait"></span><div><b>Dana Wells</b><small>England</small></div></div>
</article>
<article class="review-card" style="left:445px">
  <div class="quote-mark">“</div>
  <p>On the other hand, we denounce with righteous indignation and dislike men who are so beguiled and demoralized by the charms of pleasure of the moment, so blinded by desire, that they cannot foresee the pain and trouble that are bound .</p>
  <div class="stars">★★★★★</div>
  <div class="reviewer"><span class="avatar" role="img" aria-label="Reviewer portrait"></span><div><b>Dana Wells</b><small>England</small></div></div>
</article>
<article class="review-card" style="left:764px">
  <div class="quote-mark">“</div>
  <p>But in certain circumstances and owing to the claims of duty or the obligations of business it will frequently occur that pleasures have to be repudiated and annoyances accepted. The wise man therefore always holds in these matters.</p>
  <div class="stars">★★★★★</div>
  <div class="reviewer"><span class="avatar" role="img" aria-label="Reviewer portrait"></span><div><b>Dana Wells</b><small>England</small></div></div>
</article>
<div class="town-strip" role="img" aria-label="Faint line drawing of a row of houses along the street"></div>

<section class="contact"></section>
<h2 class="section-title" style="top:3188px">CONTACT US</h2>
<div class="title-rule" style="top:3231px"></div>
<div class="field" style="left:282px;top:3270px;width:312px;height:41px">First Name</div>
<div class="field" style="left:605px;top:3270px;width:311px;height:41px">Last Name</div>
<div class="field" style="left:282px;top:3325px;width:312px;height:41px">E mail</div>
<div class="field" style="left:605px;top:3325px;width:311px;height:41px">Phone</div>
<div class="field" style="left:282px;top:3381px;width:634px;height:134px">Description of property</div>
<div class="submit">SUBMIT</div>

<footer class="site-footer">
  <div class="brand">
    <span class="brand-mark"></span>
    <div class="brand-name"><span class="big">Bright Door</span><span class="small">Rental Management</span></div>
  </div>
  <div class="foot-head" style="left:519px">MENU</div>
  <ul class="foot-menu"><li>HOME</li><li>SERVICES</li><li>PROPERTIES</li><li>PRICING</li><li>REVIEWS</li><li>CONTACT</li></ul>

  <div class="foot-head" style="left:707px">CONTACT US</div>
  <div class="foot-item" style="left:707px;top:92px"><span class="dot"><svg width="10" height="12" viewBox="0 0 10 12"><path d="M5 0a4 4 0 014 4c0 3-4 8-4 8S1 7 1 4a4 4 0 014-4z" fill="#2b2b2b"/><circle cx="5" cy="4" r="1.5" fill="#fff"/></svg></span><span>2210 Larchmont Road<br>Calgary, AB T2P 4K1</span></div>
  <div class="foot-item" style="left:707px;top:143px"><span class="dot"><svg width="11" height="11" viewBox="0 0 24 24"><path fill="#2b2b2b" d="M6.6 10.8a15 15 0 006.6 6.6l2.2-2.2c.3-.3.7-.4 1-.2 1.1.4 2.3.6 3.6.6.6 0 1 .4 1 1V20c0 .6-.4 1-1 1A17 17 0 013 4c0-.6.4-1 1-1h3.5c.6 0 1 .4 1 1 0 1.3.2 2.5.6 3.6.1.3 0 .7-.2 1z"/></svg></span><span>Call Us<br>587-210-4418</span></div>
  <div class="foot-item" style="left:707px;top:194px"><span class="dot"><svg width="12" height="9" viewBox="0 0 12 9"><rect x=".5" y=".5" width="11" height="8" fill="#2b2b2b"/><path d="M1 1l5 4 5-4" fill="none" stroke="#fff"/></svg></span><span>E mail Us<br>info@brightdoorstays.ca</span></div>

  <div class="foot-head" style="left:970px">FOLLOW US</div>
  <div class="foot-item" style="left:970px;top:92px"><span class="dot"></span><span>Like us on<br>FRIENDLY</span></div>
  <div class="foot-item" style="left:970px;top:143px"><span class="dot"></span><span>Follow us on<br>CHIRPER</span></div>
  <div class="foot-item" style="left:970px;top:194px"><span class="dot"></span><span>Follow us on<br>WORKLINK</span></div>
</footer>
<div class="copyright">Copyright © 2020 All Rights Reserved</div>

</body>
</html>
```